New company generic tri fold brochure

We are a new small business looking to reach as many potential customers as possible for a low price. We do a variety of self-defense and protection seminars that can be customized to fit the needs of church groups, corporations, community organizations, and families. We do not teach karate, we teach awareness and common self-defense movements that can be instinctively used after just a few hours of training. We believe that self-defense is not only a right, it is your responsibility.

Our preliminary seminar is called Ready for Tomorrow - This is an innovative self-defense and situational awareness personal safety training program. We focus on the predator mindset, tactics and conflict avoidance. We provide seminar attendees with our Easy, Effective, and Practical Personal Protection and life Skills tools to detect, dissuade and defeat a predator. Our goals are to teach everyone to act under extreme stress and respond instinctively using simple, real & practical everyday actions.

Our seminars do not teach “Martial Arts”. We recognize that most people don’t have the time or desire to fully embrace the concepts taught in most karate schools. The skills learned under those controlled situations will more than likely desert us in a crisis. When the body is conditioned, but not the mind, fight or flight will kick in. The bloodstream is flooded with adrenaline, vision and hearing are affected, and the mind fills with a sea of emotions. We simply can’t think normally under those circumstances. We will train you to use techniques instinctively to get you out of dangerous situations.

Everyone has the right to protect themselves and should be able to find a fun, energetic, and educational program that works with their interest, budget and time. Personal and Family protection is not an option….It’s a responsibility. Our martial art science will help you look after yourself and family. 

We also have specialized seminars for women's rape prevention, children's safety and bully handling, weapons training, personal and family protection, and professional defensive & protective procedures.

Our main professor is Carl Hoskins who has almost 40 years of learning and teaching self defense to all ages. We are in the process of setting up our website with more information and seminar dates. When it is ready for public viewing the site name is www.brightguardcourses.net. (GUARD stands for Guided Understanding And Rapid Departure).

I am attaching our main logo and some pictures we have used in the past. We prefer lighter backgrounds and royal blue lettering and accents.

Target Market(s)

Adult men and women ages 18 - 50.

Industry/Entity Type

Education

Font styles to use
Other font styles liked:
• Verdana

Colors
0455a3
ec1f27
ffffff
f04a51
3277b5
33a6d7

Requirements
Must have
• Web address - www.brightguardcourses.net
• Contact Information - Carl Hoskins - ProfessorCarl@brightguardcourses.net (208) 555-0173 and Monica Hoskins - Monica@brightguardcourses.net (208) 555-0186
• Uploaded logo. Brief description of Ready For Tomorrow with emphasis on our ability to customize the seminars to fit any family or group
Should not have
• We are trying to de-emphasize the karate aspect of self-defense. We are NOT a karate school and the seminars we teach do not require any prior knowledge of karate. We use easy to learn, simple, and instinctive moves to avoid confrontations and escape from an attacker.

```html
<!DOCTYPE html>
<html lang="en">
<head>
<meta charset="utf-8">
<title>Brightguard Courses – Tri-fold Inside</title>
<link rel="stylesheet" href="https://fonts.googleapis.com/css2?family=Open+Sans:ital,wght@0,400;0,700;1,700&display=swap">
<style>
  :root {
    --royal: #2f4a9e;
    --orange: #e9591c;
    --orange-light: #f07a2a;
    --paper: #ffffff;
    --ink-blue: #2b4a9c;
    --stage: #e6e6e6;
  }
  * { box-sizing: border-box; margin: 0; padding: 0; }
  html, body { width: 1200px; height: 800px; overflow: hidden; }
  body {
    background: var(--stage);
    font-family: "Open Sans", Verdana, sans-serif;
    position: relative;
  }
  .brochure {
    position: absolute; left: 30px; top: 30px;
    width: 1140px; height: 740px;
    display: grid; grid-template-columns: repeat(3, 1fr);
    box-shadow: 0 6px 18px rgba(0,0,0,.18);
  }
  .panel { position: relative; overflow: hidden; display: flex; flex-direction: column; }
  .photo { flex: none; }

  /* Panel 1 – professor */
  .panel--about { background: var(--royal); }
  .panel--about .photo {
    height: 380px;
    background: linear-gradient(160deg, #7a8f5a 0%, #d9dcd6 45%, #3b3a3a 100%);
  }
  .name-tag {
    align-self: flex-start;
    background: var(--orange);
    color: #fff; font-weight: 700; font-size: 21px; line-height: 1.1;
    padding: 8px 26px 8px 22px; margin-top: -44px; position: relative;
  }
  .about-copy { color: #fff; font-size: 14px; line-height: 1.45; padding: 14px 24px 0; }
  .about-copy p + p { margin-top: 12px; }
  .figure-strip {
    margin: auto 24px 22px; height: 86px; background: var(--paper);
    display: flex; align-items: center; justify-content: center;
    flex: none;
  }
  .figure-strip .art {
    width: 78%; height: 68px;
    background: linear-gradient(90deg, #23364f, #b8342f, #23364f, #b8342f);
    opacity: .85;
  }

  /* Panel 2 – program */
  .panel--program { background: var(--paper); }
  .program-copy {
    color: var(--ink-blue); font-size: 14px; line-height: 1.45;
    padding: 32px 30px 18px; text-align: justify; flex: 1;
  }
  .program-copy p + p { margin-top: 14px; }
  .panel--program .photo {
    height: 250px;
    background: linear-gradient(120deg, #ece8e4 0%, #b9a79a 40%, #2a2a2a 75%, #b7a7a0 100%);
  }

  /* Panel 3 – groups */
  .panel--groups { background: linear-gradient(180deg, var(--orange) 0%, var(--orange-light) 100%); }
  .groups-intro { color: #fff; font-size: 14px; line-height: 1.45; padding: 32px 26px 18px; }
  .panel--groups .photo {
    height: 250px;
    background: linear-gradient(180deg, #6fa6d4 0%, #bcd3e4 45%, #b59d7b 60%, #8a7660 100%);
  }
  .section-tag {
    align-self: flex-end; width: 88%;
    background: var(--paper); color: var(--ink-blue);
    font-weight: 700; font-style: italic; font-size: 21px;
    padding: 10px 20px; margin-top: -30px; position: relative;
  }
  .groups-copy { color: #fff; font-size: 14px; line-height: 1.45; padding: 22px 26px 0; text-align: justify; }
</style>
</head>
<body>
  <main class="brochure">
    <section class="panel panel--about">
      <div class="photo" role="img" aria-label="Photo of the professor in a suit leaning on a white car"></div>
      <h2 class="name-tag">Professor<br>Carl Hoskins</h2>
      <div class="about-copy">
        <p>My wife, Monica, and I established Brightguard Courses as a positive way to use my 39 years of Martial Arts, personal protection training and knowledge to reach as many people both casual and professional, as possible.</p>
        <p>We believe that everyone should know how to protect themselves and their family, regardless of income level, physical ability, or age.</p>
      </div>
      <div class="figure-strip">
        <div class="art" role="img" aria-label="Illustration of blue and red figures practising self-defense moves"></div>
      </div>
    </section>

    <section class="panel panel--program">
      <div class="program-copy">
        <p>Ready for Tomorrow is an innovative self-defense and situational awareness personal safety training program. We focus on the predator mindset, tactics and conflict avoidance. We provide seminar attendees with our Easy, Effective, and Practical Personal Protection and Life skills to detect, dissuade, and defeat a predator.</p>
        <p>Our goals are to teach everyone to act under extreme stress and respond instinctively using simple, real &amp; practical everyday actions.</p>
        <p>Our seminars do not teach “Martial Arts”. We recognize that most people don’t have the time or desire to fully embrace the concept taught in most karate schools. The skills learned under those controlled situations will most likely desert us in a crisis. We will train you to use techniques instinctively to get you out of dangerous situations.</p>
      </div>
      <div class="photo" role="img" aria-label="Photo of an instructor demonstrating an arm escape with a student"></div>
    </section>

    <section class="panel panel--groups">
      <p class="groups-intro">Empower yourself and attain a higher level of self-confidence with this one-of-a-kind personal protection or weapon seminars that will teach you life-saving skills. All courses provide hands-on training courses that can be easily learned in a few short hours.</p>
      <div class="photo" role="img" aria-label="Photo of two men at outdoor weapons training on open ground"></div>
      <h2 class="section-tag">Group Safety Training</h2>
      <p class="groups-copy">Brightguard Courses is happy to work with you to customize our content to fit your audience’s needs whether you are a small business, University, Corporation, or religious organization for men and/or women. We focus on conflict avoidance and you will learn many tools to discourage predators from attacking. These programs are highly rated and will create a buzz of conversation among all who attend.</p>
    </section>
  </main>
</body>
</html>
```